Looking for a web design for event planning. Targeting the Wedding Industry, Corporate Meetings, Special Events, Fundraisers and other Celebratory Events
Home Page - name with pictures of various events- 3 buttons to go to
Wedding ( engagement parties, bridal showers, rehearsal dinners, welcome receptions and wedding receptions page
Corporate Meetings/Fundraisers page
Special Events/Celebratory Events
Updates

Target Market(s)

Brides, Wedding Planners, Corporate Event Planners, Destination Companies, Public

Industry/Entity Type

Event Planning

Contact Information for Business Card

name , phone number and email address
images of party images...wedding cake- balloons-party hat etc

Logo Text

Dana Ruth Korvatch Event Design @ The Bayview Harbor Rowing Society

Number of Pages Required

4 page

Font styles to use
Decorative

Colors

Designer to choose colors to be used in the design.

Requirements
Must have
• Dana Ruth Korvatch Event Design
• @ Bayview Harbor Rowing Society
• 415-555-0193
• drkeventstudio@example-mail.net
• back side of card - Image of Bayview Harbor Rowing Society
Nice to have
• fun and catchy party images
• wedding cake - diamond ring -balloons - party hat- flowers
• would like to see the images in white, gold and silver
Should not have
• photographic pictures

```html
<!DOCTYPE html>
<html lang="en">
<head>
<meta charset="utf-8">
<title>Dana Ruth Korvatch Event Design</title>
<link href="https://fonts.googleapis.com/css2?family=Pacifico&family=Poppins:wght@400;500;600&display=swap" rel="stylesheet">
<style>
:root{
  --gold:#d2b43a;
  --gold-light:#e9d67a;
  --ink:#111;
  --text:#333;
  --muted:#8a8a8a;
  --white:#fff;
  --footer:#0c0c0c;
  --footer-bar:#1b1b1b;
}
*{margin:0;padding:0;box-sizing:border-box}
html,body{width:1200px;height:4036px;overflow:hidden}
body{position:relative;font-family:"Poppins",sans-serif;color:var(--text);background:var(--white)}
.abs{position:absolute}
.script{font-family:"Pacifico",cursive}
.btn{position:absolute;background:var(--gold);color:var(--ink);border-radius:30px;display:flex;align-items:center;justify-content:center;font-weight:500}

/* top bar */
.topbar{left:0;top:0;width:1200px;height:48px;background:var(--gold);display:flex;align-items:center;justify-content:flex-end;padding-right:94px;gap:12px;color:var(--white);font-size:15px}
.topbar .sq{width:20px;height:20px;background:var(--white);border-radius:3px}
.topbar .info{display:flex;align-items:center;gap:6px;margin-right:8px}

/* nav */
.nav{left:0;top:48px;width:1200px;height:87px;display:flex;align-items:center;gap:36px;padding-left:98px;font-size:17px;color:var(--ink);font-weight:500}

/* hero */
.hero{left:0;top:135px;width:1200px;height:578px;background:linear-gradient(180deg,#4b3626 0%,#6b4b30 45%,#3a2a1e 100%)}
.hero-shade{left:0;top:135px;width:1200px;height:578px;background:rgba(30,18,10,.35)}
.hero-title{left:0;top:250px;width:1200px;text-align:center;color:var(--white);font-size:52px}
.hero-text{left:230px;top:333px;width:740px;text-align:center;color:var(--white);font-size:17px;line-height:38px;font-weight:500}
.hero .btn{}
.badge{left:528px;top:649px;width:144px;height:144px;border-radius:50%;background:var(--gold);border:4px solid var(--white)}
.badge-art{left:563px;top:684px;width:74px;height:74px;border-radius:50%;background:#e2cb63}

/* welcome */
.welcome-1{left:0;top:870px;width:1200px;text-align:center;font-size:42px;color:var(--ink)}
.welcome-2{left:0;top:945px;width:1200px;text-align:center;font-size:40px;font-weight:600;color:var(--ink)}

/* service cards */
.card{top:1087px;width:329px;height:474px;background:var(--white);box-shadow:0 4px 14px rgba(0,0,0,.22)}
.card-photo{left:0;top:0;width:100%;height:199px}
.card-icon{position:absolute;left:126px;top:172px;width:76px;height:76px;border-radius:50%;background:#e6e6e6;border:4px solid var(--white)}
.card h3{position:absolute;top:254px;width:100%;text-align:center;font-size:23px;font-weight:500;color:var(--ink)}
.card p{position:absolute;left:16px;top:296px;width:297px;text-align:center;font-size:14px;line-height:25px;color:var(--text)}
.card .btn{left:84px;top:413px;width:161px;height:46px;font-size:16px;color:var(--white)}

/* about */
.ring{border-radius:50%;background:var(--gold)}
.about-title{left:624px;top:1680px;font-size:40px;font-weight:500;color:var(--ink)}
.about-text{left:624px;top:1752px;width:480px;font-size:16px;line-height:30px}

/* events */
.section-title{left:0;width:1200px;text-align:center;font-size:40px;font-weight:500;color:var(--ink)}
.ev{border-radius:50%;background:var(--white);box-shadow:0 0 22px rgba(0,0,0,.13);text-align:center}
.ev h4{position:absolute;width:100%;top:158px;font-size:20px;font-weight:500;color:var(--ink)}
.ev p{position:absolute;left:60px;right:60px;top:204px;font-size:14px;line-height:27px;color:var(--muted)}
.ev-icon{position:absolute;left:50%;top:60px;width:84px;height:78px;margin-left:-42px;border-radius:12px;background:#e4e4e4}
.chev{width:54px;height:54px;border-radius:50%;background:#d9d9d9;display:flex;align-items:center;justify-content:center}

/* blog */
.blog-main{left:94px;top:2890px;width:614px;height:339px;border-radius:14px;background:linear-gradient(135deg,#3d2a2e,#8a4a5a 45%,#6f7a3c 80%,#b3b0a8)}
.blog-title{left:94px;top:3270px;font-size:34px;font-weight:600;color:var(--ink)}
.blog-text{left:94px;top:3326px;width:640px;font-size:17px;line-height:30px}
.side{left:786px;width:320px;height:161px;border-radius:8px;overflow:hidden}
.side span{position:absolute;left:0;bottom:0;width:100%;padding:8px 8px 10px;font-size:14px;line-height:21px;color:var(--white);background:rgba(200,170,50,.75)}

/* footer */
.footer{left:0;top:3614px;width:1200px;height:347px;background:var(--footer);color:var(--white)}
.footer h5{position:absolute;font-size:24px;font-weight:500}
.footer p,.footer li{font-size:15px;line-height:29px}
.footer ul{list-style:none;position:absolute}
.f-circle{position:absolute;width:36px;height:36px;border-radius:50%;border:2px solid var(--white)}
.contact-row{position:absolute;left:786px;display:flex;gap:22px;align-items:flex-start}
.contact-row .ic{width:36px;height:36px;border-radius:50%;border:2px solid var(--white);display:flex;align-items:center;justify-content:center;flex:none}
.bottom{left:0;top:3961px;width:1200px;height:75px;background:var(--footer-bar);color:var(--white);font-size:16px;display:flex;align-items:center;justify-content:center}
.bottom .code{position:absolute;right:44px;font-weight:600}
</style>
</head>
<body>

<div class="abs topbar">
  <div class="info">
    <svg width="16" height="16" viewBox="0 0 24 24"><path d="M6.6 10.8a15 15 0 0 0 6.6 6.6l2.2-2.2c.3-.3.7-.4 1-.2 1.1.4 2.3.6 3.6.6.6 0 1 .4 1 1V20c0 .6-.4 1-1 1A17 17 0 0 1 3 4c0-.6.4-1 1-1h3.5c.6 0 1 .4 1 1 0 1.3.2 2.5.6 3.6.1.3 0 .7-.2 1z" fill="#fff"/></svg>
    415-555-0193
  </div>
  <div class="info">
    <svg width="18" height="14" viewBox="0 0 18 14"><rect x="1" y="1" width="16" height="12" fill="none" stroke="#fff" stroke-width="1.6"/><path d="M1 1l8 7 8-7" fill="none" stroke="#fff" stroke-width="1.6"/></svg>
    drkeventstudio@example-mail.net
  </div>
  <span class="sq"></span><span class="sq"></span><span class="sq"></span><span class="sq"></span><span class="sq"></span>
</div>

<nav class="abs nav">
  <span>Home</span><span>About Us</span><span>Wedding</span><span>Corporate Meetings</span><span>Fundraisers</span><span>Special Events</span><span>Celebratory Events</span><span>Contact Us</span>
</nav>

<section>
  <div class="abs hero" role="img" aria-label="Banquet hall with set dinner tables and warm lighting"></div>
  <div class="abs hero-shade"></div>
  <h1 class="abs hero-title script">Dana Ruth Korvatch Event.</h1>
  <p class="abs hero-text">Lorem Ipsum is simply dummy text of the printing and typesetting industry. Lorem Ipsum has been the industry's standard dummy text ever since the 1500s.</p>
  <a class="btn" style="left:516px;top:427px;width:168px;height:60px;font-size:21px">Read More</a>
  <div class="abs badge"></div>
  <div class="abs badge-art" role="img" aria-label="Toasting glasses icon"></div>
</section>

<section>
  <h2 class="abs welcome-1 script" style="font-weight:400">Welcome To</h2>
  <h2 class="abs welcome-2">Dana Ruth Korvatch Event.</h2>

  <article class="abs card" style="left:89px">
    <div class="abs card-photo" role="img" aria-label="Event stage lit in purple" style="background:linear-gradient(135deg,#4a1466,#b23bd6 55%,#d9a8f0)"></div>
    <div class="card-icon" role="img" aria-label="Calendar icon"></div>
    <h3>Events</h3>
    <p>Lorem Ipsum is simply dummy text of the printing and typesetting industry. Lorem Ipsum has been the industry's</p>
    <a class="btn">Read More</a>
  </article>
  <article class="abs card" style="left:430px">
    <div class="abs card-photo" role="img" aria-label="Dining table set in blue light" style="background:linear-gradient(135deg,#0e1430,#253a78 55%,#5a6a9a)"></div>
    <div class="card-icon" role="img" aria-label="Food and drinks icon"></div>
    <h3>Food &amp; Drinks</h3>
    <p>Lorem Ipsum is simply dummy text of the printing and typesetting industry. Lorem Ipsum has been the industry's</p>
    <a class="btn">Read More</a>
  </article>
  <article class="abs card" style="left:775px">
    <div class="abs card-photo" role="img" aria-label="Candlelit venue table" style="background:linear-gradient(135deg,#2a0e06,#8a3a12 50%,#e08a3a)"></div>
    <div class="card-icon" role="img" aria-label="Bottle icon"></div>
    <h3>Venues</h3>
    <p>Lorem Ipsum is simply dummy text of the printing and typesetting industry. Lorem Ipsum has been the industry's</p>
    <a class="btn">Read More</a>
  </article>
</section>

<section>
  <div class="abs ring" style="left:89px;top:1682px;width:188px;height:188px"></div>
  <div class="abs" role="img" aria-label="Costumed guest at an event" style="left:99px;top:1692px;width:168px;height:168px;border-radius:50%;background:linear-gradient(135deg,#7a2a1a,#c9a050)"></div>
  <div class="abs ring" style="left:108px;top:1865px;width:188px;height:188px"></div>
  <div class="abs" role="img" aria-label="Red roses bouquet" style="left:118px;top:1875px;width:168px;height:168px;border-radius:50%;background:linear-gradient(135deg,#5a0a0a,#d42020 60%,#3a5020)"></div>
  <div class="abs ring" style="left:215px;top:1655px;width:350px;height:350px"></div>
  <div class="abs" role="img" aria-label="Portrait of the event designer" style="left:230px;top:1670px;width:320px;height:320px;border-radius:50%;background:linear-gradient(135deg,#e6ddd2,#b89a78 55%,#6a5442)"></div>

  <h2 class="abs about-title">About Us</h2>
  <p class="abs about-text">Lorem Ipsum is simply dummy text of the printing and typesetting industry. Lorem Ipsum has been the industry's standard dummy text ever since the 1500s, when an unknown printer took a galley of type and scrambled it to make a type specimen book. It has survived not only five centuries, but also the leap into electronic typesetting, remaining essentially unchanged.</p>
  <a class="btn" style="left:624px;top:1994px;width:163px;height:46px;font-size:16px;color:var(--white)">Read More</a>
</section>

<section>
  <h2 class="abs section-title" style="top:2136px">Our Events</h2>

  <div class="abs ev" style="left:96px;top:2290px;width:356px;height:356px">
    <div class="ev-icon" role="img" aria-label="Wedding couple icon"></div>
    <h4>Weddings</h4>
    <p>Lorem Ipsum is simply dummy text of the printing and typesetting industry.</p>
  </div>
  <div class="abs ev" style="left:756px;top:2290px;width:356px;height:356px">
    <div class="ev-icon" role="img" aria-label="Celebration masks icon"></div>
    <h4>Celebratory Events</h4>
    <p>Lorem Ipsum is simply dummy text of the printing and typesetting industry.</p>
  </div>

  <svg class="abs" style="left:380px;top:2248px" width="440" height="440" viewBox="0 0 440 440">
    <circle cx="220" cy="220" r="214" fill="none" stroke="#f3e9b8" stroke-width="3"/>
    <circle cx="220" cy="220" r="206" fill="none" stroke="#efe09a" stroke-width="4"/>
    <circle cx="220" cy="220" r="197" fill="#fbf5dc" stroke="#e9d67a" stroke-width="5"/>
    <circle cx="220" cy="220" r="184" fill="#d2b43a" stroke="#fff" stroke-width="4"/>
  </svg>
  <div class="abs" style="left:416px;top:2284px;width:368px;height:368px;text-align:center">
    <div class="abs" role="img" aria-label="Meeting group icon" style="left:142px;top:38px;width:84px;height:84px;border-radius:12px;background:#c29f22"></div>
    <h4 class="abs" style="left:0;top:154px;width:100%;font-size:20px;font-weight:500;color:var(--ink)">Corporate Meetings</h4>
    <p class="abs" style="left:84px;top:200px;width:200px;font-size:14px;line-height:27px;color:var(--ink)">Lorem Ipsum is simply dummy text of the printing and typesetting industry.</p>
  </div>

  <div class="abs chev" style="left:248px;top:2618px">
    <svg width="14" height="20" viewBox="0 0 14 20"><path d="M3 3l7 7-7 7" fill="none" stroke="#d2b43a" stroke-width="3"/></svg>
  </div>
  <div class="abs chev" style="left:908px;top:2618px">
    <svg width="14" height="20" viewBox="0 0 14 20"><path d="M3 3l7 7-7 7" fill="none" stroke="#d2b43a" stroke-width="3"/></svg>
  </div>
  <div class="abs chev" style="left:570px;top:2640px;width:60px;height:60px;background:#000">
    <svg width="16" height="22" viewBox="0 0 16 22"><path d="M4 3l8 8-8 8" fill="none" stroke="#fff" stroke-width="3.5"/></svg>
  </div>
</section>

<section>
  <h2 class="abs section-title" style="top:2770px">Blog</h2>
  <div class="abs blog-main" role="img" aria-label="Table flower arrangement with greenery"></div>
  <h3 class="abs blog-title">Lorem Ipsum dolar sit</h3>
  <p class="abs blog-text">Lorem Ipsum is simply dummy text of the printing and typesetting industry. Lorem Ipsum has been the industry's standard dummy text ever since the 1500s, when an unknown printer took a galley of type and scrambled it to make a type specimen book.</p>
  <a class="btn" style="left:89px;top:3469px;width:183px;height:58px;font-size:20px;color:var(--white)">Read More</a>

  <div class="abs side" style="top:2890px;background:linear-gradient(135deg,#3a2418,#8a5a3a)" role="img" aria-label="Guests at a banquet"><span>Lorem Ipsum is simply dummy text of the printing and typesetting industry.</span></div>
  <div class="abs side" style="top:3068px;background:linear-gradient(135deg,#4a3a2a,#c4b090)" role="img" aria-label="Plated catering dish"><span>Lorem Ipsum is simply dummy text of the printing and typesetting industry.</span></div>
  <div class="abs side" style="top:3248px;background:linear-gradient(135deg,#2e3a22,#b02020 60%,#5a6a40)" role="img" aria-label="Red bird in a decorated tree"><span>Lorem Ipsum is simply dummy text of the printing and typesetting industry.</span></div>
</section>

<footer class="abs footer">
  <h5 style="left:106px;top:40px">About Us</h5>
  <p class="abs" style="left:97px;top:94px;width:330px">Lorem Ipsum is simply dummy text of the printing and typesetting industry. Lorem Ipsum has been the industry's standard dummy text ever since the 1500s</p>
  <span class="f-circle" style="left:112px;top:232px"></span>
  <span class="f-circle" style="left:158px;top:232px"></span>
  <span class="f-circle" style="left:206px;top:232px"></span>

  <h5 style="left:523px;top:36px">Information</h5>
  <ul style="left:525px;top:92px">
    <li>Home</li><li>About Us</li><li>Wedding</li><li>Fundraisers</li><li>Special Events</li><li>Celebratory Events</li><li>Contact Us</li>
  </ul>

  <h5 style="left:786px;top:36px">Contact Us</h5>
  <div class="contact-row" style="top:102px">
    <span class="ic"><svg width="14" height="18" viewBox="0 0 14 18"><path d="M7 1a6 6 0 0 0-6 6c0 4.5 6 10 6 10s6-5.5 6-10a6 6 0 0 0-6-6z" fill="none" stroke="#fff" stroke-width="1.6"/><circle cx="7" cy="7" r="2" fill="#fff"/></svg></span>
    <p>Address :<br>1740 Harborview Lane<br>Ste 310, Oakland, CA 94607</p>
  </div>
  <div class="contact-row" style="top:194px">
    <span class="ic"><svg width="16" height="16" viewBox="0 0 24 24"><path d="M6.6 10.8a15 15 0 0 0 6.6 6.6l2.2-2.2c.3-.3.7-.4 1-.2 1.1.4 2.3.6 3.6.6.6 0 1 .4 1 1V20c0 .6-.4 1-1 1A17 17 0 0 1 3 4c0-.6.4-1 1-1h3.5c.6 0 1 .4 1 1 0 1.3.2 2.5.6 3.6.1.3 0 .7-.2 1z" fill="#fff"/></svg></span>
    <p>Call Us :<br><span style="font-size:17px;font-weight:500">415-555-0193</span></p>
  </div>
  <div class="contact-row" style="top:266px">
    <span class="ic"><svg width="16" height="12" viewBox="0 0 18 14"><rect x="1" y="1" width="16" height="12" fill="none" stroke="#fff" stroke-width="1.6"/><path d="M1 1l8 7 8-7" fill="none" stroke="#fff" stroke-width="1.6"/></svg></span>
    <p>E - Mail :<br>drkeventstudio@example-mail.net</p>
  </div>
</footer>

<div class="abs bottom">
  Copyright 2019 | All Rights Reserved | Privacy Policy | Term &amp; Conditions
  <span class="code">C34</span>
</div>

</body>
</html>
```